Business card, folder, and other items for LMV
Lakemoor Vale Oncology, PLLC business cards and material
Please show us folder designs that will house these documents as well.
Thanks for all the great designs.
After seeing double sided designs above, we would like to utilize this design feature. Please submit double sided designs. Thank you.
Please show designs of folder and stationery as well. Current designs look very nice. Thanks for the submissions.

```html
<!DOCTYPE html>
<html lang="en">
<head>
<meta charset="utf-8">
<title>LMV – Business Cards</title>
<link rel="stylesheet" href="https://fonts.googleapis.com/css2?family=Arimo:wght@400;700&display=swap">
<style>
  :root {
    --page: #ececec;
    --blue-light: #3a6fc4;
    --blue-dark: #1c3c8c;
    --brand-ink: #1c3c8c;
    --white: #ffffff;
    --ink-soft: #dfe8fb;
  }
  * { margin: 0; padding: 0; box-sizing: border-box; }
  html, body { width: 1200px; height: 852px; overflow: hidden; background: var(--page); }
  body { position: relative; font-family: "Arimo", Arial, sans-serif; }

  .card {
    position: absolute;
    width: 520px; height: 300px;
    border-radius: 18px;
    overflow: hidden;
    background: var(--white);
    box-shadow: 0 6px 18px rgba(0,0,0,0.18);
  }
  .card--front { left: 80px; top: 110px; }
  .card--back  { left: 600px; top: 440px; }
  .card__bg { position: absolute; inset: 0; width: 100%; height: 100%; }

  .brand {
    position: absolute; top: 0; height: 300px;
    display: flex; align-items: center; justify-content: center;
  }
  .card--front .brand { left: 300px; width: 220px; }
  .card--back .brand { left: 0; width: 220px; }
  .brand__name {
    font-weight: 400; font-size: 44px; line-height: 1;
    color: var(--brand-ink); letter-spacing: 2px;
  }

  .info { position: absolute; color: var(--white); }
  .card--front .info { left: 24px; }
  .card--back .info { right: 24px; text-align: right; }
  .info--person { top: 56px; }
  .person__name { font-weight: 700; font-size: 15px; }
  .person__role { font-size: 12px; color: var(--ink-soft); margin-top: 3px; }
  .info--contact { top: 168px; font-size: 11.5px; line-height: 1.45; color: var(--ink-soft); }
  .address { margin-bottom: 10px; }
  .contact-line { display: flex; align-items: center; gap: 6px; }
  .card--back .contact-line { justify-content: flex-end; }
  .icon { width: 12px; height: 12px; flex: none; }
</style>
</head>
<body>

  <section class="card card--front" aria-label="Business card, front">
    <svg class="card__bg" viewBox="0 0 520 300" preserveAspectRatio="none" aria-hidden="true">
      <defs>
        <linearGradient id="blueFront" x1="0" y1="0" x2="1" y2="1">
          <stop offset="0" stop-color="#3a6fc4"/>
          <stop offset="1" stop-color="#1c3c8c"/>
        </linearGradient>
        <linearGradient id="bandFront" x1="0" y1="0" x2="1" y2="0">
          <stop offset="0" stop-color="#a9adb5"/>
          <stop offset="1" stop-color="#eceef1"/>
        </linearGradient>
      </defs>
      <path d="M0 0 H318 C280 90 280 210 318 300 H0 Z" fill="url(#bandFront)"/>
      <path d="M0 0 H300 C262 90 262 210 300 300 H0 Z" fill="url(#blueFront)"/>
    </svg>
    <div class="info info--person">
      <p class="person__name">Mara Kherwin, M.D., DABR</p>
      <p class="person__role">President</p>
    </div>
    <div class="info info--contact">
      <p class="address">P.O. Box 2480<br>Brookfield, OH 44403-2480</p>
      <p class="contact-line">
        <svg class="icon" viewBox="0 0 12 12" aria-hidden="true"><circle cx="6" cy="6" r="6" fill="#fff"/><path d="M3.6 3 l1.3 0 .5 1.5-.8.6a4 4 0 0 0 2.3 2.3l.6-.8 1.5.5v1.3A6 6 0 0 1 3.6 3z" fill="#1c3c8c"/></svg>
        1-555-204-7719
      </p>
      <p class="contact-line">
        <svg class="icon" viewBox="0 0 12 12" aria-hidden="true"><circle cx="6" cy="6" r="6" fill="#fff"/><circle cx="6" cy="6" r="2" fill="none" stroke="#1c3c8c" stroke-width="1.2"/><path d="M8 4v2.8a1 1 0 0 0 2 0V6a4 4 0 1 0-1.6 3.2" fill="none" stroke="#1c3c8c" stroke-width="1.1"/></svg>
        mkherwin@lakemoorvaleonc.com
      </p>
      <p class="contact-line">
        <svg class="icon" viewBox="0 0 12 12" aria-hidden="true"><circle cx="6" cy="6" r="6" fill="#fff"/><circle cx="6" cy="6" r="3.6" fill="none" stroke="#1c3c8c" stroke-width="1"/><path d="M2.4 6h7.2M6 2.4c-2 2.2-2 5 0 7.2M6 2.4c2 2.2 2 5 0 7.2" fill="none" stroke="#1c3c8c" stroke-width=".8"/></svg>
        www.lakemoorvaleonc.com
      </p>
    </div>
    <div class="brand">
      <span class="brand__name">LMV</span>
    </div>
  </section>

  <section class="card card--back" aria-label="Business card, reverse">
    <svg class="card__bg" viewBox="0 0 520 300" preserveAspectRatio="none" aria-hidden="true">
      <defs>
        <linearGradient id="blueBack" x1="1" y1="0" x2="0" y2="1">
          <stop offset="0" stop-color="#3a6fc4"/>
          <stop offset="1" stop-color="#1c3c8c"/>
        </linearGradient>
        <linearGradient id="bandBack" x1="1" y1="0" x2="0" y2="0">
          <stop offset="0" stop-color="#a9adb5"/>
          <stop offset="1" stop-color="#eceef1"/>
        </linearGradient>
      </defs>
      <path d="M520 0 H202 C240 90 240 210 202 300 H520 Z" fill="url(#bandBack)"/>
      <path d="M520 0 H220 C258 90 258 210 220 300 H520 Z" fill="url(#blueBack)"/>
    </svg>
    <div class="brand">
      <span class="brand__name">LMV</span>
    </div>
    <div class="info info--person">
      <p class="person__name">Mara Kherwin, M.D., DABR</p>
      <p class="person__role">President</p>
    </div>
    <div class="info info--contact">
      <p class="address">P.O. Box 2480<br>Brookfield, OH 44403-2480</p>
      <p class="contact-line">
        1-555-204-7719
        <svg class="icon" viewBox="0 0 12 12" aria-hidden="true"><circle cx="6" cy="6" r="6" fill="#fff"/><path d="M3.6 3 l1.3 0 .5 1.5-.8.6a4 4 0 0 0 2.3 2.3l.6-.8 1.5.5v1.3A6 6 0 0 1 3.6 3z" fill="#1c3c8c"/></svg>
      </p>
      <p class="contact-line">
        mkherwin@lakemoorvaleonc.com
        <svg class="icon" viewBox="0 0 12 12" aria-hidden="true"><circle cx="6" cy="6" r="6" fill="#fff"/><circle cx="6" cy="6" r="2" fill="none" stroke="#1c3c8c" stroke-width="1.2"/><path d="M8 4v2.8a1 1 0 0 0 2 0V6a4 4 0 1 0-1.6 3.2" fill="none" stroke="#1c3c8c" stroke-width="1.1"/></svg>
      </p>
      <p class="contact-line">
        www.lakemoorvaleonc.com
        <svg class="icon" viewBox="0 0 12 12" aria-hidden="true"><circle cx="6" cy="6" r="6" fill="#fff"/><circle cx="6" cy="6" r="3.6" fill="none" stroke="#1c3c8c" stroke-width="1"/><path d="M2.4 6h7.2M6 2.4c-2 2.2-2 5 0 7.2M6 2.4c2 2.2 2 5 0 7.2" fill="none" stroke="#1c3c8c" stroke-width=".8"/></svg>
      </p>
    </div>
  </section>

</body>
</html>
```